Design a Coloring Book Cover

Please help us create a 8.5 x 11 inch coloring book cover. As you can tell from the title, it is a Christian adult coloring book.

Title: Sparrow Window Pages
Subtitle: The Inspirational Christian Adult Coloring Book (Religious Themes and Inspiring Phrases)

You can look at some covers here for some ideas...http://www.shelvoria-market.example/s/ref=nb_sb_ss_i_1_11?url=search-alias%3Dstripbooks&field-keywords=christian+coloring+books&sprefix=christian+c%2Cstripbooks%2C252

```html
<!DOCTYPE html>
<html lang="en">
<head>
<meta charset="utf-8">
<title>Sparrow Window Pages – Coloring Book Cover</title>
<link rel="stylesheet" href="https://fonts.googleapis.com/css2?family=Norican&family=Kaushan+Script&family=Dancing+Script:wght@600;700&display=swap">
<style>
  :root {
    --cream: #f4ebcf;
    --paper: #fbfaf6;
    --navy: #15296b;
    --red: #ee1c25;
    --banner: #f6f5f0;
    --banner-line: #eaa0a3;
    --petal: #f0a7a6;
    --petal-peach: #f2b596;
    --leaf: #6aa57a;
  }
  * { margin: 0; padding: 0; box-sizing: border-box; }
  html, body { width: 928px; height: 1200px; overflow: hidden; }
  body { background: var(--paper); }
  .cover {
    position: relative;
    width: 928px;
    height: 1200px;
    overflow: hidden;
    background: linear-gradient(to right,
      var(--cream) 0, var(--cream) 278px,
      var(--paper) 278px, var(--paper) 660px,
      var(--cream) 660px, var(--cream) 928px);
  }
  .rule {
    position: absolute;
    left: 0; right: 0;
    display: flex;
    align-items: center;
    gap: 8px;
  }
  .rule::before, .rule::after {
    content: "";
    flex: 1;
    border-top: 2px dashed var(--navy);
  }
  .rule--top { top: 72px; }
  .rule--bottom { top: 1070px; }
  .series-label {
    font-family: "Dancing Script", cursive;
    font-weight: 700;
    font-size: 40px;
    color: var(--navy);
    line-height: 1;
  }
  .theme-line {
    font-family: "Dancing Script", cursive;
    font-weight: 700;
    font-size: 31px;
    color: var(--navy);
    line-height: 1;
  }
  .floral-art, .banner { position: absolute; left: 0; top: 0; }
  .title {
    position: absolute;
    left: 0; right: 0;
    top: 345px;
    text-align: center;
    font-family: "Norican", cursive;
    font-weight: 400;
    line-height: 142px;
  }
  .title span { display: block; }
  .title .word--navy { color: var(--navy); font-size: 128px; }
  .title .word--red { color: var(--red); font-size: 132px; }
  .subtitle {
    position: absolute;
    left: 0; right: 0;
    top: 996px;
    text-align: center;
    font-family: "Kaushan Script", cursive;
    font-size: 37px;
    color: var(--red);
    line-height: 1;
  }
</style>
</head>
<body>
<main class="cover">
  <div class="rule rule--top"><span class="series-label">Coloring Book</span></div>

  <svg class="floral-art" width="928" height="1200" viewBox="0 0 928 1200" role="img" aria-label="Watercolor bouquet of pink and peach roses with green leaves framing the title banner">
    <defs>
      <radialGradient id="bouquet" cx="50%" cy="50%" r="55%">
        <stop offset="0" stop-color="var(--petal-peach)"/>
        <stop offset="0.55" stop-color="var(--petal)"/>
        <stop offset="0.85" stop-color="var(--leaf)" stop-opacity="0.7"/>
        <stop offset="1" stop-color="var(--leaf)" stop-opacity="0"/>
      </radialGradient>
    </defs>
    <ellipse cx="464" cy="545" rx="500" ry="385" fill="url(#bouquet)" opacity="0.85"/>
  </svg>

  <svg class="banner" width="928" height="1200" viewBox="0 0 928 1200" aria-hidden="true">
    <polygon points="0,443 237,309 722,309 928,433 928,670 701,815 232,815 0,670" fill="var(--banner)"/>
    <polygon points="0,462 242,325 717,325 928,452 928,651 696,799 237,799 0,651" fill="none" stroke="var(--banner-line)" stroke-width="2.5"/>
  </svg>

  <h1 class="title">
    <span class="word--navy">Sparrow</span>
    <span class="word--navy">Window</span>
    <span class="word--red">Pages</span>
  </h1>

  <p class="subtitle">The Inspirational Christian Adult Coloring Book</p>
  <div class="rule rule--bottom"><span class="theme-line">Religious Themes and Inspiring Phrases</span></div>
</main>
</body>
</html>
```